Please use the logo / design elements and font to design a business card that is eye catching and informative. If using "Direct Primary Care" logo element, you don't have to spell it out in the text.

Dr. Marcus Pellam
Vale Wellness - Direct Primary Care
4817 Tindell Rd. Suite 305
Harlow Springs, AR 71234
Phone: 555-318-7240
ValeWellnessAR.example

```html
<!DOCTYPE html>
<html lang="en">
<head>
<meta charset="UTF-8">
<title>Vale Wellness – Business Card</title>
<link rel="stylesheet" href="https://fonts.googleapis.com/css2?family=Poppins:wght@400;500;600;700&display=swap">
<style>
  :root {
    --navy: #0b1742;
    --navy-deep: #081236;
    --sky: #2bb3ec;
    --white: #ffffff;
    --ink: #0f1a3c;
    --backdrop: #4a4a4c;
  }
  * { margin: 0; padding: 0; box-sizing: border-box; }
  html, body {
    width: 1200px; height: 1200px; overflow: hidden;
    background: var(--backdrop);
    font-family: "Poppins", sans-serif;
  }
  .canvas { position: relative; width: 1200px; height: 1200px; }

  .card {
    position: absolute; left: 150px;
    width: 900px; height: 514px;
    border-radius: 32px; overflow: hidden;
    box-shadow: 0 18px 40px rgba(0,0,0,.35);
  }
  .card--front { top: 50px; background: var(--white); }
  .card--back { top: 630px; background: var(--navy); border-bottom: 4px solid var(--sky); }

  .front-bands { position: absolute; left: 0; bottom: 0; width: 900px; height: 70px; }

  .holder-name {
    position: absolute; left: 90px; top: 218px;
    font-size: 38px; font-weight: 700; letter-spacing: 1px; line-height: 1;
    color: var(--navy); text-transform: uppercase;
  }
  .contact-list { position: absolute; left: 90px; top: 274px; list-style: none; }
  .contact-item {
    display: flex; align-items: flex-start; gap: 18px;
    font-size: 25px; line-height: 37px; color: var(--ink); font-weight: 400;
  }
  .contact-icon { width: 30px; height: 30px; flex: 0 0 30px; margin-top: 3px; }

  .brand { position: absolute; display: flex; flex-direction: column; align-items: flex-end; }
  .brand--front { right: 60px; top: 70px; }
  .brand-name { display: flex; align-items: center; gap: 14px; font-weight: 600; line-height: 1; }
  .brand--front .brand-name { font-size: 56px; color: var(--navy); }
  .brand-dot { border-radius: 50%; background: var(--sky); }
  .brand--front .brand-dot { width: 20px; height: 20px; }
  .brand-tagline {
    display: flex; align-items: center; gap: 12px;
    font-weight: 600; letter-spacing: .5px; margin-top: 10px;
  }
  .brand-tagline::before, .brand-tagline::after {
    content: ""; display: block; height: 2px; background: currentColor; opacity: .7;
  }
  .brand--front .brand-tagline { font-size: 18px; color: var(--navy); }
  .brand--front .brand-tagline::before { width: 90px; }
  .brand--front .brand-tagline::after { width: 70px; }

  .back-texture {
    position: absolute; inset: 0;
    background: radial-gradient(ellipse at center, #101d4d 0%, var(--navy-deep) 80%);
  }
  .brand--back { left: 50%; top: 50%; transform: translate(-50%, -50%); align-items: center; }
  .brand--back .brand-name { font-size: 56px; color: var(--white); }
  .brand--back .brand-dot { width: 20px; height: 20px; }
  .brand--back .brand-tagline { font-size: 18px; color: var(--white); }
  .brand--back .brand-tagline::before, .brand--back .brand-tagline::after { width: 60px; }
</style>
</head>
<body>
<main class="canvas">

  <section class="card card--front" aria-label="Business card front">
    <svg class="front-bands" viewBox="0 0 900 70" preserveAspectRatio="none" aria-hidden="true">
      <polygon points="0,40 590,40 572,70 0,70" fill="var(--sky)"/>
      <polygon points="612,14 900,14 900,70 594,70" fill="var(--navy)"/>
    </svg>

    <div class="brand brand--front">
      <div class="brand-name"><span class="brand-dot" aria-hidden="true"></span>Vale Wellness</div>
      <div class="brand-tagline">Direct Primary Care</div>
    </div>

    <h1 class="holder-name">Dr. Marcus Pellam</h1>

    <ul class="contact-list">
      <li class="contact-item">
        <svg class="contact-icon" viewBox="0 0 24 24" aria-hidden="true">
          <path fill="var(--sky)" d="M6.6 10.8a15.1 15.1 0 0 0 6.6 6.6l2.2-2.2a1 1 0 0 1 1-.25 11.4 11.4 0 0 0 3.6.57 1 1 0 0 1 1 1V20a1 1 0 0 1-1 1A17 17 0 0 1 3 4a1 1 0 0 1 1-1h3.5a1 1 0 0 1 1 1c0 1.25.2 2.45.57 3.57a1 1 0 0 1-.25 1z"/>
        </svg>
        <span>555-318-7240</span>
      </li>
      <li class="contact-item">
        <svg class="contact-icon" viewBox="0 0 24 24" aria-hidden="true" fill="none" stroke="var(--sky)" stroke-width="1.8">
          <circle cx="12" cy="12" r="9.5"/>
          <ellipse cx="12" cy="12" rx="4.2" ry="9.5"/>
          <line x1="2.5" y1="12" x2="21.5" y2="12"/>
          <path d="M4.2 7h15.6M4.2 17h15.6"/>
        </svg>
        <span>ValeWellnessAR.example</span>
      </li>
      <li class="contact-item">
        <svg class="contact-icon" viewBox="0 0 24 24" aria-hidden="true">
          <path fill="var(--sky)" d="M12 2a7 7 0 0 0-7 7c0 5.2 7 13 7 13s7-7.8 7-13a7 7 0 0 0-7-7zm0 9.5A2.5 2.5 0 1 1 12 6.5a2.5 2.5 0 0 1 0 5z"/>
        </svg>
        <span>4817 Tindell Rd. Suite 305<br>Harlow Springs, AR 71234</span>
      </li>
    </ul>
  </section>

  <section class="card card--back" aria-label="Business card back">
    <div class="back-texture" role="img" aria-label="Navy background with a faint embossed repeat of the brand name"></div>
    <div class="brand brand--back">
      <div class="brand-name"><span class="brand-dot" aria-hidden="true"></span>Vale Wellness</div>
      <div class="brand-tagline">Direct Primary Care</div>
    </div>
  </section>

</main>
</body>
</html>
```